Property developer, money partner needs business card design using logo concept provided

Our company develops residential properties, does money lends for joint ventures in property deals and finds property deals for other money partners. We have provided a basic logo for you to work from. Any graphic or logo design on the card is to communicate development and finance collaboration. Color choice is not so important for us, but color choice does need to reflect professionalism.

```html
<!DOCTYPE html>
<html lang="en">
<head>
<meta charset="utf-8">
<title>Keystone Property Solutions – Business Card</title>
<link href="https://fonts.googleapis.com/css2?family=Montserrat:wght@400;500;700&display=swap" rel="stylesheet">
<style>
  :root {
    --backdrop: #e4e4e4;
    --card: #f7f7f7;
    --navy: #1d3f8f;
    --brand-blue: #1b5fb0;
    --accent-blue: #0a74c4;
    --text-grey: #4a4a4a;
    --muted-grey: #5f5f5f;
    --faint: #e2e5ec;
  }
  * { margin: 0; padding: 0; box-sizing: border-box; }
  html, body { width: 1200px; height: 1200px; overflow: hidden; }
  body {
    background: var(--backdrop);
    font-family: "Montserrat", Arial, sans-serif;
    position: relative;
  }
  .card {
    position: absolute;
    left: 235px;
    width: 730px;
    height: 417px;
    background: var(--card);
    box-shadow: 0 1px 3px rgba(0,0,0,0.18);
    overflow: hidden;
  }
  .card--front { top: 160px; }
  .card--back { top: 632px; }

  .brand { position: absolute; text-align: center; }
  .brand__mark {
    display: block;
    margin: 0 auto;
    border-radius: 50%;
    background: var(--brand-blue);
  }
  .brand__name {
    color: var(--brand-blue);
    font-weight: 700;
    letter-spacing: 0.12em;
    text-transform: uppercase;
    line-height: 1.25;
  }
  .brand__acn {
    color: var(--text-grey);
    font-weight: 400;
    letter-spacing: 0.18em;
  }

  .card--front .brand { left: 0; right: 0; top: 70px; }
  .card--front .brand__mark { width: 170px; height: 170px; margin-bottom: 30px; }
  .card--front .brand__name { font-size: 22px; }
  .card--front .brand__acn { font-size: 10px; margin-top: 8px; }

  .card--back .brand { left: 40px; width: 160px; top: 40px; }
  .card--back .brand__mark { width: 96px; height: 96px; margin-bottom: 18px; }
  .card--back .brand__name { font-size: 11px; }
  .card--back .brand__acn { font-size: 6px; margin-top: 4px; }

  .person { position: absolute; right: 60px; top: 40px; text-align: right; }
  .person__name { color: var(--navy); font-size: 30px; font-weight: 700; letter-spacing: -0.01em; }
  .person__title { color: var(--muted-grey); font-size: 18px; font-weight: 400; margin-top: 6px; }

  .tab {
    position: absolute; right: 0; top: 45px;
    width: 23px; height: 59px;
    background: var(--accent-blue);
    border-radius: 8px 0 0 8px;
  }

  .address {
    position: absolute; left: 58px; top: 232px;
    color: var(--text-grey); font-size: 18px; line-height: 27px; font-style: normal;
  }
  .contacts { position: absolute; left: 58px; top: 292px; list-style: none; }
  .contacts li {
    display: flex; align-items: center; gap: 10px;
    color: var(--text-grey); font-size: 18px; height: 27.5px;
  }
  .contacts svg { width: 16px; height: 16px; flex: none; }

  .deco-circle {
    position: absolute; right: 60px; bottom: 40px;
    width: 170px; height: 170px; border-radius: 50%;
    border: 6px solid var(--faint);
  }
</style>
</head>
<body>
  <section class="card card--front">
    <div class="brand">
      <span class="brand__mark"></span>
      <p class="brand__name">Keystone<br>Property Solutions</p>
      <p class="brand__acn">A.C.N 418 903 216</p>
    </div>
  </section>

  <section class="card card--back">
    <div class="brand">
      <span class="brand__mark"></span>
      <p class="brand__name">Keystone<br>Property Solutions</p>
      <p class="brand__acn">A.C.N 418 903 216</p>
    </div>

    <div class="person">
      <h1 class="person__name">Daniel Ashford</h1>
      <p class="person__title">Founder &amp; Director</p>
    </div>
    <div class="tab"></div>

    <address class="address">4178 Harbor Lane<br>Riverton Oregon 20457</address>

    <ul class="contacts">
      <li>
        <svg viewBox="0 0 24 24" aria-hidden="true"><path fill="#1d3f8f" d="M6.6 10.8a15.1 15.1 0 0 0 6.6 6.6l2.2-2.2a1 1 0 0 1 1-.25 11.4 11.4 0 0 0 3.6.57 1 1 0 0 1 1 1V20a1 1 0 0 1-1 1A17 17 0 0 1 3 4a1 1 0 0 1 1-1h3.5a1 1 0 0 1 1 1c0 1.25.2 2.45.57 3.57a1 1 0 0 1-.25 1z"/></svg>
        (555)-304-2718
      </li>
      <li>
        <svg viewBox="0 0 24 24" aria-hidden="true"><rect x="2" y="5" width="20" height="14" rx="1" fill="#1d3f8f"/><path d="M3 6l9 7 9-7" fill="none" stroke="#f7f7f7" stroke-width="1.8"/></svg>
        info@keystonesolutions.co
      </li>
      <li>
        <svg viewBox="0 0 24 24" aria-hidden="true"><g fill="none" stroke="#1d3f8f" stroke-width="2"><circle cx="12" cy="12" r="9.5"/><ellipse cx="12" cy="12" rx="4" ry="9.5"/><path d="M2.5 12h19M4 7h16M4 17h16"/></g></svg>
        www.keystonesolutions.co
      </li>
    </ul>

    <div class="deco-circle" aria-hidden="true"></div>
  </section>
</body>
</html>
```